Web form face-lift for an online startup

We are a web startup building a SaaS application for the freight industry. The project is mainly dedicated to the paint the main form that our customer are using along the search results that the they get. All details are in the attached documents.
Updates
The application serves the Freight Forwarders community so please think towards this industry when using background images, banners, colors, icons, etc. Computer and technology images are irrelevant.
Customer fields at the top of the page is actually part of the form.
Target Market(s)
Usually business users (Sales people, procurement, shippers, freight forwarders). Some are less tech savvy and some appreciate the new trendy web apps.
Industry/Entity Type
Building
Colors
Designer to choose colors to be used in the design.
Look and feel
Each slider illustrates characteristics of the customer's brand and the style your logo design should communicate.

```html
<!DOCTYPE html>
<html lang="en">
<head>
<meta charset="utf-8">
<title>SAAS application – Search for Quotes</title>
<link href="https://fonts.googleapis.com/css2?family=Montserrat:wght@400;500;600;700&display=swap" rel="stylesheet">
<style>
:root{
  --header-bg:#333333;
  --header-text:#ffffff;
  --header-muted:#bdbdbd;
  --accent:#f39200;
  --page-bg:#f4f4f4;
  --lower-bg:#f8f8f8;
  --text:#2b2b2b;
  --label:#3a3a3a;
  --placeholder:#a8a8a8;
  --field-border:#cfcfcf;
  --field-bg:#ffffff;
  --panel-bg:#e4f5fb;
  --panel-border:#c8e0ea;
  --select-top:#f3f3f3;
  --select-bottom:#dedede;
  --btn-top:#ffd26a;
  --btn-bottom:#f5a623;
  --btn-border:#e39a1d;
  --green:#5bb82a;
  --footer-bg:#333333;
  --footer-text:#e0e0e0;
  --hazard:#d6202a;
}
*{box-sizing:border-box;margin:0;padding:0}
html,body{width:1200px;height:1024px;overflow:hidden}
body{position:relative;background:var(--page-bg);font-family:"Montserrat",Arial,sans-serif;color:var(--text);font-size:11px}
.abs{position:absolute}

/* Header */
.site-header{position:absolute;left:0;top:0;width:1200px;height:66px;background:var(--header-bg);box-shadow:0 2px 4px rgba(0,0,0,.25)}
.app-name{position:absolute;left:161px;top:18px;font-size:23px;color:var(--header-text);font-weight:400;letter-spacing:.2px}
.app-name b{font-weight:700}
.util-nav{position:absolute;top:10px;font-size:11px;color:var(--header-muted)}
.util-nav .caret{display:inline-block;border:4px solid transparent;border-top:5px solid var(--header-muted);border-bottom:0;margin-left:2px;vertical-align:1px}
.user-name{color:var(--accent)}
.brand-dot{position:absolute;left:476px;top:30px;width:26px;height:26px;border-radius:50%;background:#fff;border:3px solid #555}
.main-nav{position:absolute;top:38px;font-size:11px;color:var(--header-text)}

/* Upper form area */
.upper{position:absolute;left:0;top:66px;width:1200px;height:684px;background:var(--page-bg)}
h1.section-title,h2.section-title{position:absolute;left:161px;font-size:18px;font-weight:500;color:var(--text)}
.label{position:absolute;font-size:11px;font-weight:600;color:var(--label)}
.field{position:absolute;height:30px;background:var(--field-bg);border:1px solid var(--field-border);border-radius:3px;box-shadow:inset 0 1px 2px rgba(0,0,0,.08);font-size:11px;color:var(--placeholder);padding:0 8px;display:flex;align-items:center}
.field.center{justify-content:center}
.field.filled{color:#777}
.field.grey{background:#f1f1f1}
.select{position:absolute;height:30px;border:1px solid #c4c4c4;border-radius:3px;background:linear-gradient(var(--select-top),var(--select-bottom));font-size:11px;font-weight:600;color:var(--label);padding:0 10px;display:flex;align-items:center;justify-content:space-between}
.select::after{content:"";border:4px solid transparent;border-top:5px solid #666;border-bottom:0}
.checkbox{position:absolute;width:12px;height:12px;border:1px solid #bdbdbd;background:#fff;border-radius:2px}
.radio{position:absolute;width:13px;height:13px;border:1px solid #bdbdbd;background:#fff;border-radius:50%}

.cargo-tab{position:absolute;top:238px;height:62px;background:#fff;border:1px solid #dcdcdc;border-bottom:none;border-radius:4px 4px 0 0}
.cargo-tab.active{background:var(--panel-bg);border-color:var(--panel-border);height:64px;z-index:2}
.tab-art{position:absolute;left:50%;top:10px;transform:translateX(-50%);border-radius:3px}
.link{position:absolute;color:var(--accent);font-weight:600;font-size:12px}

.units-panel{position:absolute;left:161px;top:300px;width:877px;height:216px;background:var(--panel-bg);border:1px solid var(--panel-border);border-radius:0 3px 3px 3px}
.btn-add{position:absolute;height:30px;border:1px solid var(--btn-border);border-radius:3px;background:linear-gradient(var(--btn-top),var(--btn-bottom));font-size:10.5px;font-weight:600;color:#3a2a00;display:flex;align-items:center;justify-content:center;box-shadow:0 1px 2px rgba(0,0,0,.15)}
.panel-divider{position:absolute;left:177px;top:452px;width:845px;height:1px;background:var(--panel-border)}

.route-banner{position:absolute;left:161px;top:556px;width:877px;height:153px;border:1px solid #222;background:linear-gradient(180deg,#2c2c2c 0%,#474747 45%,#2a2a2a 100%)}
.route-label{position:absolute;font-size:13px;font-weight:600;color:#fff}
.route-field{position:absolute;left:236px;width:583px;height:34px;background:#fff;border-radius:3px;font-size:11px;color:var(--placeholder);padding:0 9px;display:flex;align-items:center}

/* Lower options area */
.lower{position:absolute;left:0;top:750px;width:1200px;height:232px;background:var(--lower-bg);box-shadow:inset 0 6px 8px -6px rgba(0,0,0,.15);border-top:1px solid #e6e6e6}
.opt-text{position:absolute;font-size:11.5px;font-weight:500;color:var(--label)}
.hazard{position:absolute;width:16px;height:16px;border-radius:50%;border:2px solid var(--hazard);background:#fff}
.hazard::after{content:"";position:absolute;left:3px;top:3px;width:6px;height:6px;border-radius:50%;background:#222}
.btn-search{position:absolute;left:433px;top:889px;width:186px;height:47px;border-radius:24px;border:1px solid var(--btn-border);background:linear-gradient(var(--btn-top),var(--btn-bottom));font-size:15px;font-weight:700;color:#3a2a00;letter-spacing:.5px;display:flex;align-items:center;justify-content:center;box-shadow:0 2px 3px rgba(0,0,0,.2)}

/* Footer */
.site-footer{position:absolute;left:0;top:982px;width:1200px;height:42px;background:var(--footer-bg)}
.footer-link{position:absolute;top:15px;font-size:11px;color:var(--footer-text)}
.social{position:absolute;top:14px;width:14px;height:14px;border-radius:50%;background:#9a9a9a}
</style>
</head>
<body>

<header class="site-header">
  <div class="app-name"><b>SAAS</b> application</div>
  <div class="util-nav" style="left:874px">USD<span class="caret"></span></div>
  <div class="util-nav" style="left:919px">English<span class="caret"></span></div>
  <div class="util-nav user-name" style="left:983px">User name</div>
  <div class="brand-dot"></div>
  <nav>
    <span class="main-nav" style="left:523px">Menu Item 1</span>
    <span class="main-nav" style="left:613px">Menu Item 2</span>
    <span class="main-nav" style="left:703px">Menu Item 3</span>
    <span class="main-nav" style="left:789px">Menu Item 4</span>
    <span class="main-nav" style="left:876px">Menu Item 5</span>
    <span class="main-nav" style="left:972px">Menu Item 6</span>
  </nav>
</header>

<main>
  <section class="upper"></section>
  <h1 class="section-title" style="top:107px">Search for Quotes</h1>
  <span class="label" style="left:161px;top:147px">Customer</span>
  <div class="field" style="left:223px;top:139px;width:389px;height:31px"></div>
  <span class="checkbox" style="left:161px;top:184px"></span>
  <span class="label" style="left:181px;top:183px">Rate Quote?</span>

  <!-- cargo type tabs -->
  <div class="cargo-tab active" style="left:161px;width:77px">
    <div class="tab-art" role="img" aria-label="Cardboard box" style="width:50px;height:38px;background:linear-gradient(160deg,#e2c896,#b48f5a)"></div>
  </div>
  <div class="cargo-tab" style="left:245px;width:62px">
    <div class="tab-art" role="img" aria-label="Shipping container" style="width:46px;height:34px;background:linear-gradient(160deg,#4cae4c,#237a23)"></div>
  </div>
  <div class="cargo-tab" style="left:314px;width:62px">
    <div class="tab-art" role="img" aria-label="Wrapped parcel" style="width:40px;height:36px;background:linear-gradient(160deg,#f0506e,#c0182f)"></div>
  </div>
  <span class="link" style="left:384px;top:266px">More</span>

  <!-- units panel -->
  <div class="units-panel"></div>
  <span class="label" style="left:179px;top:330px">Qty</span>
  <span class="label" style="left:256px;top:330px">Stackabel</span>
  <span class="label" style="left:326px;top:330px">Load</span>
  <span class="label" style="left:527px;top:330px">Length</span>
  <span class="label" style="left:601px;top:330px">Width</span>
  <span class="label" style="left:676px;top:330px">Height</span>
  <span class="label" style="left:815px;top:330px">Weight</span>

  <div class="field center" style="left:178px;top:353px;width:60px">5</div>
  <span class="checkbox" style="left:279px;top:362px"></span>
  <div class="select" style="left:325px;top:353px;width:186px">Box/Pallet</div>
  <div class="field center" style="left:526px;top:353px;width:61px">100</div>
  <div class="field center" style="left:600px;top:353px;width:61px">100</div>
  <div class="field center" style="left:674px;top:353px;width:61px">100</div>
  <div class="select" style="left:751px;top:353px;width:47px;padding:0 7px">Cm</div>
  <div class="field" style="left:814px;top:353px;width:168px;border-radius:3px 0 0 3px">Box/Pallet</div>
  <div class="select" style="left:980px;top:353px;width:42px;padding:0 6px;border-radius:0 3px 3px 0">Kg</div>

  <div class="btn-add" style="left:178px;top:407px;width:108px">+ Add more units</div>
  <div class="panel-divider"></div>

  <span class="label" style="left:559px;top:478px;font-size:12px">Total</span>
  <div class="field center" style="left:596px;top:469px;width:61px">5</div>
  <div class="field grey" style="left:673px;top:469px;width:116px;border-radius:3px 0 0 3px">1</div>
  <div class="select" style="left:787px;top:469px;width:52px;padding:0 7px;border-radius:0 3px 3px 0">CBM</div>
  <div class="field filled" style="left:854px;top:469px;width:108px;border-radius:3px 0 0 3px">100</div>
  <div class="select" style="left:960px;top:469px;width:60px;padding:0 8px;border-radius:0 3px 3px 0">Kg</div>

  <!-- route -->
  <div class="route-banner" role="img" aria-label="Container port with stacked shipping containers"></div>
  <span class="route-label" style="left:192px;top:583px">From:</span>
  <div class="route-field" style="top:572px">Shipping address or port</div>
  <svg class="abs" style="left:508px;top:620px" width="20" height="24" viewBox="0 0 20 24" aria-hidden="true">
    <path d="M6 0h8v12h6L10 24 0 12h6z" fill="var(--green)"/>
  </svg>
  <span class="route-label" style="left:210px;top:666px">To:</span>
  <div class="route-field" style="top:655px">Shipping address or port</div>

  <!-- options -->
  <section class="lower"></section>
  <h2 class="section-title" style="top:784px">Options</h2>
  <span class="radio" style="left:161px;top:817px"></span>
  <span class="opt-text" style="left:182px;top:817px">Import</span>
  <span class="radio" style="left:238px;top:817px"></span>
  <span class="opt-text" style="left:259px;top:817px">Export</span>
  <span class="opt-text" style="left:314px;top:817px">Incoterm: <span style="color:var(--accent);font-weight:600">FCA</span></span>

  <span class="checkbox" style="left:522px;top:818px"></span>
  <span class="hazard" style="left:539px;top:815px" aria-label="Hazard class 1"></span>
  <span class="checkbox" style="left:579px;top:818px"></span>
  <span class="hazard" style="left:596px;top:815px" aria-label="Hazard class 2"></span>
  <span class="checkbox" style="left:634px;top:818px"></span>
  <span class="hazard" style="left:651px;top:815px" aria-label="Hazard class 3"></span>

  <div class="select" style="left:812px;top:809px;width:226px">Price Level</div>
  <span class="link" style="left:955px;top:844px">More Options</span>

  <div class="btn-search">SEARCH QUOTES</div>
  <span class="opt-text" style="left:628px;top:906px;font-weight:600">or</span>
  <span class="link" style="left:647px;top:906px">Create Manually</span>
</main>

<footer class="site-footer">
  <span class="footer-link" style="left:161px">About Us</span>
  <span class="footer-link" style="left:223px">Privacy policy</span>
  <span class="footer-link" style="left:308px">Terms of Service</span>
  <span class="footer-link" style="left:407px">News</span>
  <span class="social" style="left:926px" aria-label="Feed"></span>
  <span class="social" style="left:951px" aria-label="Social link"></span>
  <span class="social" style="left:976px" aria-label="Social link"></span>
  <span class="social" style="left:1000px" aria-label="Social link"></span>
  <span class="social" style="left:1024px" aria-label="Social link"></span>
</footer>

</body>
</html>
```